Poster advertising a workshop on digital analytics

Poster to market a workshop I'm presenting. I work in digital analytics and my workshop will talk about how analytics used to be done and what's changed. People will be able to go to heaps of different workshops so I need a poster to make mine stand out.

Attachments:
* Poster copy to use.
* Two headshots you can use, select the one that best fits your design.
* Company logo
* Example of the poster wall from last years' conference, to give you an idea.

Poster specs:
A2 size at a portrait orientation
420mm x 594mm
5mm Bleed with Crop Marks
CMYK

Target Market(s)

Marketers

Industry/Entity Type

Marketing

Font styles to use
Serif
Sans Serif

Colors

Designer to choose colors to be used in the design.

Requirements
Must have
• Eye catching

```html
<!DOCTYPE html>
<html lang="en">
<head>
<meta charset="utf-8">
<title>Analytics Has Changed, Have You? – Workshop Poster</title>
<link rel="stylesheet" href="https://fonts.googleapis.com/css2?family=Fredoka:wght@600&family=Cabin:wght@400;500&display=swap">
<style>
  :root {
    --stage: #ececec;
    --orange: #d97a3c;
    --orange-deep: #c4632a;
    --ring: #f2c12e;
    --paper: #ffffff;
    --ink: #2e2e2e;
    --brand-blue: #4a9bd6;
    --skin-light: #fff6ec;
    --skin: #f1cfae;
    --skin-warm: #d99a6c;
    --shirt: #5fb0b8;
    --shirt-deep: #3f8f99;
  }
  * { box-sizing: border-box; margin: 0; padding: 0; }
  html, body {
    width: 1200px; height: 960px; overflow: hidden;
    background: var(--stage);
  }
  .poster {
    position: absolute; left: 282px; top: 30px;
    width: 636px; height: 900px;
    background: var(--orange);
    overflow: hidden;
    box-shadow: 0 4px 18px rgba(0,0,0,.18);
    font-family: "Cabin", "Helvetica Neue", Arial, sans-serif;
    color: var(--ink);
  }
  .brand-disc {
    position: absolute; left: 429px; top: -101px;
    width: 234px; height: 234px; border-radius: 50%;
    background: var(--paper);
  }
  .brand-name {
    position: absolute; left: 452px; top: 30px; width: 180px;
    text-align: center; color: var(--brand-blue);
    font-weight: 500; font-size: 21px; line-height: 1.1;
  }
  .portrait {
    position: absolute; left: 0; top: 380px; width: 636px; height: 520px;
  }
  .bubble {
    position: absolute; border-radius: 50%;
    background: var(--paper);
    border: 7px solid var(--ring);
  }
  .bubble--intro { left: 164px; top: 52px; width: 306px; height: 306px; }
  .bubble--topics { left: 9px; top: 244px; width: 228px; height: 228px; }
  .bubble--presenter { left: 397px; top: 234px; width: 228px; height: 228px; }
  .heading {
    position: absolute; text-align: center;
    font-family: "Fredoka", "Arial Rounded MT Bold", sans-serif;
    font-weight: 600; text-transform: uppercase;
    color: var(--orange);
    -webkit-text-stroke: 6px var(--paper);
    paint-order: stroke fill;
  }
  .heading .lead { color: var(--paper); -webkit-text-stroke: 6px var(--orange-deep); }
  .heading--main { left: 80px; top: 28px; width: 480px; font-size: 30px; line-height: 35px; }
  .heading--topics { left: 24px; top: 230px; width: 200px; font-size: 28px; line-height: 33px; }
  .heading--presenter { left: 411px; top: 230px; width: 200px; font-size: 28px; line-height: 33px; }
  .copy {
    position: absolute; text-align: center;
    font-size: 12.2px; line-height: 16px;
  }
  .copy--intro { left: 176px; top: 146px; width: 282px; }
  .copy--topics { left: 23px; top: 302px; width: 200px; list-style: none; }
  .copy--presenter { left: 411px; top: 302px; width: 200px; }
</style>
</head>
<body>
  <main class="poster">
    <svg class="portrait" viewBox="0 0 636 520" role="img" aria-label="Headshot photograph of the presenter, smiling, in a teal t-shirt">
      <defs>
        <radialGradient id="portrait-tone" cx="0.5" cy="0.45" r="0.6">
          <stop offset="0" stop-color="var(--skin-light)"/>
          <stop offset="0.55" stop-color="var(--skin)"/>
          <stop offset="1" stop-color="var(--skin-warm)"/>
        </radialGradient>
        <linearGradient id="shirt-tone" x1="0" y1="0" x2="0" y2="1">
          <stop offset="0" stop-color="var(--shirt)"/>
          <stop offset="1" stop-color="var(--shirt-deep)"/>
        </linearGradient>
      </defs>
      <path d="M0 520 V470 Q90 418 236 418 Q322 458 408 418 Q550 418 636 470 V520 Z" fill="url(#shirt-tone)" stroke="var(--ring)" stroke-width="4"/>
      <path d="M166 250 Q162 8 322 0 Q482 8 480 250 Q472 362 404 402 L404 432 Q322 458 240 432 L240 402 Q172 362 166 250 Z" fill="url(#portrait-tone)" stroke="var(--ring)" stroke-width="4"/>
    </svg>

    <div class="brand-disc"></div>
    <div class="brand-name">Frostline<br>Analytics</div>

    <div class="bubble bubble--intro"></div>
    <div class="bubble bubble--topics"></div>
    <div class="bubble bubble--presenter"></div>

    <h1 class="heading heading--main"><span class="lead">Analytics</span><br>has changed,<br>have you ?</h1>
    <h2 class="heading heading--topics"><span class="lead">We'll</span><br>cover :</h2>
    <h2 class="heading heading--presenter"><span class="lead">The</span><br>presenter</h2>

    <p class="copy copy--intro">Analytics isn't the afterthought it once<br>was, but has rapidly become the driver of<br>digital businesses. Tools have got more<br>sophisticated and practices have improved the<br>reliability and breadth of what's recorded. Is<br>your business still stuck doing it the 1990s<br>way, and what can you do about it? Elliot<br>walks through the evolution of digital<br>analytics, how to do things properly<br>today and where things are<br>headed.</p>

    <ul class="copy copy--topics">
      <li>Your grandmother's<br>Digital Analytics</li>
      <li>Tag management to move fast</li>
      <li>Data assurance to prevent<br>breaking things</li>
      <li>Tool improvements and changes</li>
      <li>How to get to the new world<br>of modern digital<br>analytics</li>
    </ul>

    <p class="copy copy--presenter">Elliot Marsh has been<br>doing Internet stuff for 25<br>years and got into digital<br>analytics while trying to<br>understand what people were<br>doing on web sites and why. He<br>loves joining the dots between<br>different sets of data in<br>order to tell a story.</p>
  </main>
</body>
</html>
```